Brightvale Circuit

Marion T Hadley
"Title" Adventure Manager & Host
2817 North 9th Street | Vancouver, BC | V5R 2K8
Direct 604.582. 1907 x 215
Skype drum41
1.800.436.5127
brightvale.ca
(perhaps small steady route bureau logo somewhere? Or “Powered by SRB”?)
- Grey/white logo cut out on reverse of card with web address

Industry/Entity Type

Travel

```html
<!DOCTYPE html>
<html lang="en">
<head>
<meta charset="utf-8">
<title>Marion T Hadley – Brightvale Circuit</title>
<link rel="stylesheet" href="https://fonts.googleapis.com/css2?family=Didact+Gothic&display=swap">
<style>
  :root {
    --card-bg: #3a4546;
    --ink: #ffffff;
  }
  html, body {
    margin: 0;
    padding: 0;
    width: 1200px;
    height: 702px;
    overflow: hidden;
    background: var(--card-bg);
  }
  .business-card {
    position: relative;
    width: 1200px;
    height: 702px;
    background: var(--card-bg);
    color: var(--ink);
    font-family: "Didact Gothic", "Century Gothic", sans-serif;
  }
  .card-line {
    position: absolute;
    left: 76px;
    margin: 0;
    line-height: 1;
    white-space: nowrap;
    font-weight: 400;
  }
  .holder-name { top: 118px; font-size: 48px; }
  .holder-title { top: 184px; font-size: 48px; }
  .contact { font-size: 42px; }
  .contact-address { top: 312px; }
  .contact-direct { top: 367px; }
  .contact-skype { top: 422px; }
  .contact-tollfree { top: 477px; }
  .contact-web { top: 532px; }
  .powered-by { top: 609px; font-size: 25px; }
</style>
</head>
<body>
  <main class="business-card">
    <h1 class="card-line holder-name">Marion T Hadley</h1>
    <p class="card-line holder-title">Adventure Manager &amp; Host</p>
    <p class="card-line contact contact-address">2817 North 9th Street | Vancouver, BC | V5R 2K8</p>
    <p class="card-line contact contact-direct">Direct 604.582. 1907 x 215</p>
    <p class="card-line contact contact-skype">Skype drum41</p>
    <p class="card-line contact contact-tollfree">1.800.436.5127</p>
    <p class="card-line contact contact-web">brightvale.ca</p>
    <p class="card-line powered-by">Powered by SRB</p>
  </main>
</body>
</html>
```